Supplement Package and Bottle Design*

We are a supplement company rebranding a number of product ranges for which we need a designer.

We will start with two products for joint health supplementation that are part of one range.

1. QUENTIL R58 Internal Oil Drops
The internal oil drop requires a design for the outer box and inside bottle label – see attached.

Front of box should include the following text:
- QUENTIL R58
- Internal Oil Drops
- Original formula from the oils of fresh Laurus nobilis L. leaves and Curcuma longa L. rhizomes
- Dilute before use
- Food supplement
- 100ml
- Some prominent icon/ graphics indicating use for joint health
- Brenuvel logo

2. QUENTIL M4 External Cream
The external cream only requires a design for the bottle label – see attached.
- QUENTIL M4
- External Cream
- Original formula from the oils of fresh Laurus nobilis L. leaves + 7 select ingredients
- 150ml
- Brenuvel logo

Overall design:
- Common design between both products (oil drops and cream)
Must appeal to a customer base of middle-age/ seniors
- Pharmaceutical product feel with touch of nature/ herbal remedy
- Design my convey a feeling of dependability, trust, effectiveness
- Premium product feel. These are very expensive products
- Design must be easy to adapt for new product ranges
- Use icons/ symbols to indicate health application, example: icon of knee to indicate use for joints
- "R58" and "M4" should be prominent to distinguish the products
- You have a choice of two Brenuvel logos. See attached.
- Primary colours: white and rgb(33, 136, 135)
- Designers can also consider some use of stamped gold/ silver for embellishments

Once a successful design/ feel has been chosen then exact dielines will be provided.

Target Market(s)

Seniors (65+ years old) with arthritis. Generally retired and affluent.

Industry/Entity Type

Health Product

Colors
33b8a4

Requirements
Must have
• As per project description.

Please creatively use a laurel wreath in the design. Either as a standalone element or multiple laurel wreaths in the background of the design. Can be vector or blended image.

As the supplements are made from bay leaves (laurel leaves) this subtle connection should be present.
Should not have
• Should not be cheap design and loud.

Premium design that conveys trust and pharmaceutical grade treatment with embellishments reminding that this is a natural/ herbal remedy product

```html
<!DOCTYPE html>
<html lang="en">
<head>
<meta charset="utf-8">
<title>QUENTIL R58 Internal Oil Drops – Packaging</title>
<link rel="stylesheet" href="https://fonts.googleapis.com/css2?family=Cormorant+Garamond:wght@400;500&display=swap">
<style>
  :root {
    --paper: #ffffff;
    --blush-top: #e3dcdb;
    --blush-bottom: #cfc8c8;
    --teal-top: #2f9d8b;
    --teal-bottom: #23897a;
    --ink: #2b2b2b;
    --ink-soft: #4a4a4a;
    --on-teal: #1f3b36;
    --rule: rgba(30, 60, 55, 0.35);
    --icon-bg: #e7eeee;
  }
  * { box-sizing: border-box; margin: 0; padding: 0; }
  html, body { width: 1200px; height: 890px; overflow: hidden; background: var(--paper); }
  body { font-family: "Cormorant Garamond", Georgia, serif; color: var(--ink); }

  .canvas { position: relative; width: 1200px; height: 890px; }

  .panel {
    position: absolute;
    overflow: hidden;
    background: linear-gradient(180deg, var(--blush-top), var(--blush-bottom));
  }
  .box-front { left: 250px; top: 210px; width: 220px; height: 450px; }
  .box-side  { left: 470px; top: 210px; width: 220px; height: 450px; }
  .bottle-label { left: 760px; top: 310px; width: 300px; height: 250px; }

  .brand { position: absolute; left: 0; right: 0; text-align: center; }
  .brand-mark {
    display: block; margin: 0 auto 10px;
    width: 50px; height: 50px; border-radius: 50%;
    border: 1.5px solid var(--ink);
  }
  .brand-name {
    font-size: 15px; font-weight: 500; letter-spacing: 3px;
    text-transform: uppercase; color: var(--ink);
  }

  .headline {
    position: absolute; left: 14px; right: 10px;
    font-size: 25px; font-weight: 400; letter-spacing: -0.5px;
    white-space: nowrap; color: var(--ink);
  }
  .headline .code { font-size: 27px; }

  .teal-band {
    position: absolute; left: 0; right: 0; bottom: 0;
    background: linear-gradient(180deg, var(--teal-top), var(--teal-bottom));
    color: var(--on-teal);
  }
  .form-name { font-size: 13px; letter-spacing: 0.6px; text-transform: uppercase; }
  .tagline { font-size: 12px; }

  .use-icon {
    position: absolute; width: 70px; height: 70px;
    border-radius: 8px; background: var(--icon-bg);
    border: 1.5px solid rgba(255,255,255,0.8);
  }

  .spec-row {
    position: absolute; left: 10px; right: 10px;
    display: flex; align-items: center; justify-content: space-between;
    font-size: 7px; border-top: 1px solid var(--rule); padding-top: 5px;
  }
  .sprig { display: block; width: 26px; height: 12px; background: #1f4d45; border-radius: 50%; opacity: 0.75; }

  .copy { font-size: 8.5px; line-height: 1.25; }
  .spec-grid { position: absolute; left: 10px; right: 10px; font-size: 8px; }
  .spec-grid .row { display: flex; justify-content: space-between; border-top: 1px solid var(--rule); padding: 4px 0; }
  .spec-grid .row span + span { border-left: 1px solid var(--rule); padding-left: 6px; }
</style>
</head>
<body>
<main class="canvas">

  <!-- Box front -->
  <section class="panel box-front" aria-label="Box front">
    <div class="brand" style="top:40px">
      <span class="brand-mark"></span>
      <span class="brand-name">Brenuvel</span>
    </div>
    <h1 class="headline" style="top:245px">QUENTIL<span class="code">R58</span></h1>
    <div class="teal-band" style="height:167px">
      <p class="form-name" style="position:absolute;left:14px;top:12px">Internal Oil Drops</p>
      <p class="tagline" style="position:absolute;left:32px;top:30px">natural remedies</p>
      <div class="use-icon" role="img" aria-label="Knee joint icon showing joint health use" style="left:30px;top:50px"></div>
      <div class="spec-row" style="bottom:10px">
        <span>Food supplement</span>
        <span class="sprig" role="img" aria-label="Laurel sprig emblem"></span>
        <span>100mL | 3.38 fl. oz</span>
      </div>
    </div>
  </section>

  <!-- Box side -->
  <section class="panel box-side" aria-label="Box side">
    <div class="brand" style="top:40px">
      <span class="brand-mark"></span>
      <span class="brand-name">Brenuvel</span>
    </div>
    <h2 class="headline" style="top:245px">QUENTIL<span class="code">R58</span></h2>
    <div class="teal-band" style="height:167px">
      <p class="form-name" style="position:absolute;left:10px;top:12px">Internal Oil Drops</p>
      <p class="copy" style="position:absolute;left:10px;right:10px;top:32px">Original formula from the oils of fresh Laurus nobilis L. leaves and Curcuma longa L. rhizomes</p>
      <div class="spec-grid" style="top:76px">
        <div class="row"><span>Dilute before use</span><span>Food supplement</span></div>
        <div class="row"><span>Natural remedies</span><span>100mL | 3.38 fl. oz</span></div>
      </div>
      <span class="sprig" role="img" aria-label="Laurel sprig emblem" style="position:absolute;left:97px;bottom:18px"></span>
    </div>
  </section>

  <!-- Bottle label -->
  <section class="panel bottle-label" aria-label="Bottle label">
    <div class="brand" style="top:18px">
      <span class="brand-mark" style="width:44px;height:44px;margin-bottom:6px"></span>
      <span class="brand-name" style="font-size:13px">Brenuvel</span>
    </div>
    <h2 class="headline" style="top:94px;left:0;right:0;text-align:center;font-size:30px">QUENTIL <span class="code" style="font-size:32px">R58</span></h2>
    <div class="teal-band" style="height:110px;text-align:center">
      <p class="form-name" style="padding-top:8px;font-size:14px;letter-spacing:1.5px">Internal Oil Drops</p>
      <p class="tagline">natural remedies</p>
      <div class="spec-row" style="bottom:14px;font-size:8px">
        <span>Food supplement</span>
        <span style="display:flex;align-items:center;gap:4px;font-size:5px">Plant <span class="sprig" role="img" aria-label="Laurel sprig emblem" style="width:32px;height:13px"></span> based</span>
        <span>100mL | 3.38 fl. oz</span>
      </div>
    </div>
  </section>

</main>
</body>
</html>
```